San Francisco Pet Care Non Profit

Business Card Design for non profit organization.
We are a mobile pet care team who supports and attends to pets whose owners are homeless. Thanks for your help and creativity.

Industry/Entity Type

Non Profit

Contact Information for Business Card

Marisol Keddy
President
2871 Larkmoor Street, #512
San Francisco, CA 94187
phone: 415-729-3846
fax: 415-781-4052
marisol@tidywagonvan.org
website: tidywagonvan.org
facebook: facebook.com/TidyWagonVan

Font styles to use
Serif
Sans Serif

Colors

Designer to choose colors to be used in the design.

Requirements
Must have
• above details and attached logo

```html
<!DOCTYPE html>
<html lang="en">
<head>
<meta charset="utf-8">
<title>TidyWagonVan Business Card</title>
<link href="https://fonts.googleapis.com/css2?family=Arimo:wght@400;700&display=swap" rel="stylesheet">
<style>
  :root {
    --sky: #29a8e0;
    --sky-soft: rgba(255,255,255,0.12);
    --ink: #111111;
    --paper: #ffffff;
    --backdrop: #2b2b2d;
  }
  html, body {
    margin: 0;
    width: 1200px;
    height: 901px;
    overflow: hidden;
    background: var(--backdrop);
    font-family: "Arimo", Arial, sans-serif;
  }
  .card {
    position: absolute;
    left: 250px;
    width: 700px;
    height: 400px;
    border-radius: 28px;
    overflow: hidden;
  }
  .card-front { top: 30px; background: var(--sky); color: var(--paper); }
  .card-back { top: 471px; background: var(--paper); color: var(--ink); }

  .front-mark {
    position: absolute; right: -40px; top: -70px;
    width: 300px; height: 300px; border-radius: 50%;
    background: var(--sky-soft);
  }
  .front-brand { position: absolute; left: 150px; top: 150px; }
  .brand-name { font-weight: 700; font-size: 58px; letter-spacing: -0.5px; line-height: 1; }
  .brand-tagline { font-weight: 700; font-size: 20px; margin-top: 4px; margin-left: 60px; }
  .front-web { position: absolute; right: 70px; bottom: 60px; font-size: 17px; font-weight: 700; }

  .back-waves { position: absolute; inset: 0; }
  .back-brand { position: absolute; left: 50px; top: 45px; }
  .back-brand .brand-name { color: var(--sky); font-size: 50px; }
  .back-brand .brand-tagline { color: var(--ink); font-size: 18px; margin-left: 64px; }

  .person { position: absolute; right: 50px; top: 28px; text-align: right; }
  .person-name { font-weight: 700; font-size: 24px; }
  .person-role { font-weight: 700; font-size: 15px; color: var(--sky); }

  .address { position: absolute; left: 48px; top: 168px; font-size: 17px; font-weight: 700; line-height: 1.35; }
  .address-row { display: flex; align-items: flex-start; gap: 10px; }
  .address-row .social { color: var(--sky); }
  .dot { width: 20px; height: 20px; border-radius: 50%; background: var(--sky); flex: none; margin-top: 1px; display: flex; align-items: center; justify-content: center; }

  .contacts { position: absolute; right: 40px; top: 228px; text-align: right; color: var(--paper); font-size: 18px; font-weight: 700; line-height: 1.45; }
  .contact-row { display: flex; justify-content: flex-end; align-items: center; gap: 10px; }
  .contact-row svg { width: 22px; height: 22px; flex: none; }
</style>
</head>
<body>

<section class="card card-front">
  <div class="front-mark" aria-hidden="true"></div>
  <div class="front-brand">
    <div class="brand-name">TidyWagonVan</div>
    <div class="brand-tagline">Mobile Pet Care Team</div>
  </div>
  <div class="front-web">www.tidywagonvan.org</div>
</section>

<section class="card card-back">
  <svg class="back-waves" viewBox="0 0 700 400" aria-hidden="true">
    <defs>
      <path id="wave" d="M0,310 C200,330 300,300 380,210 C450,130 580,95 700,90 L700,460 L0,460 Z"/>
    </defs>
    <use href="#wave" fill="var(--sky)"/>
    <use href="#wave" fill="var(--paper)" y="10"/>
    <use href="#wave" fill="var(--ink)" y="18"/>
    <use href="#wave" fill="var(--paper)" y="38"/>
    <use href="#wave" fill="var(--sky)" y="48"/>
  </svg>

  <div class="back-brand">
    <div class="brand-name">TidyWagonVan</div>
    <div class="brand-tagline">Mobile Pet Care Team</div>
  </div>

  <div class="person">
    <div class="person-name">Marisol Keddy</div>
    <div class="person-role">President</div>
  </div>

  <div class="address">
    <div class="address-row"><span class="dot"></span><span class="social">TidyWagonVan</span></div>
    <div class="address-row">
      <span class="dot">
        <svg width="12" height="12" viewBox="0 0 12 12"><path d="M6 1a3.5 3.5 0 0 0-3.5 3.5C2.5 7.5 6 11 6 11s3.5-3.5 3.5-6.5A3.5 3.5 0 0 0 6 1z" fill="#fff"/><circle cx="6" cy="4.5" r="1.3" fill="var(--sky)"/></svg>
      </span>
      <span>2871 Larkmoor Street, #512<br>San Francisco, CA 94187</span>
    </div>
  </div>

  <div class="contacts">
    <div class="contact-row"><span>415-729-3846</span>
      <svg viewBox="0 0 22 22"><circle cx="11" cy="11" r="10" fill="none" stroke="#fff" stroke-width="1.5"/><path d="M7.5 6.5l2 0 1 2.5-1.3 1a6 6 0 0 0 2.8 2.8l1-1.3 2.5 1v2a1 1 0 0 1-1 1A8 8 0 0 1 6.5 7.5a1 1 0 0 1 1-1z" fill="#fff"/></svg>
    </div>
    <div class="contact-row"><span>415-781-4052</span>
      <svg viewBox="0 0 22 22"><circle cx="11" cy="11" r="10" fill="none" stroke="#fff" stroke-width="1.5"/><rect x="8" y="5.5" width="6" height="3" fill="#fff"/><rect x="5.5" y="8.5" width="11" height="5" rx="1" fill="#fff"/><rect x="8" y="12.5" width="6" height="4" fill="#fff" stroke="var(--sky)" stroke-width="0.8"/></svg>
    </div>
    <div class="contact-row"><span>marisol@tidywagonvan.org</span>
      <svg viewBox="0 0 22 22"><circle cx="11" cy="11" r="10" fill="none" stroke="#fff" stroke-width="1.5"/><rect x="5.5" y="7" width="11" height="8" fill="#fff"/><path d="M5.5 7l5.5 4.5L16.5 7" fill="none" stroke="var(--sky)" stroke-width="1"/></svg>
    </div>
    <div class="contact-row"><span>www.tidywagonvan.org</span>
      <svg viewBox="0 0 22 22"><circle cx="11" cy="11" r="10" fill="none" stroke="#fff" stroke-width="1.5"/><circle cx="11" cy="11" r="6" fill="none" stroke="#fff" stroke-width="1.2"/><ellipse cx="11" cy="11" rx="2.5" ry="6" fill="none" stroke="#fff" stroke-width="1"/><path d="M5 11h12" stroke="#fff" stroke-width="1"/></svg>
    </div>
  </div>
</section>

</body>
</html>
```